National Golf Software business needs banner ad designs

Our software company looks after golf clubs throughout the country. Our service specialises in membership billing for the clubs and tries to convince members to change from paying their fees upfront to monthly payment by direct debit. Simple catch cries like "spread the cost of your membership across the whole year", "let us help you make your membership affordable", "Ask you club how to spread the cost of your subs" etc. We are dealing with cost conscious clubs - not the top end of the market - and their members are also cost conscious. No good being too 'high brow'. We are also dealing with older members who are fearful of change and afraid of technology - we need to be safe and reassuring yet a great way to save up front costs. We need probably 5 to 10 banners that can rotate through on our website and on our mobile product.

Target Market(s)

Golfers, typically older and afraid of technology and afraid of direct debit. Existing members of golf clubs who have paid upfront for years and don't understand why they should pay a few dollars extra each month to split their payments. Sometimes their annual fees are quite low ($300 - $400) so they cannot justify the additional $3.50 per month surcharge for splitting their fees.

Industry/Entity Type

Golf Course

Requirements
Must have
• Make the member desire to spread the cost of their annual subscriptions. Safe, reliable, frees up their disposable income. Talk to the club to find out how. Safe and secure. Club administered.
Nice to have
• Option to call us directly on a 1300 582 916 number - they will still need to go back to the club to fill in and lodge the paperwork.
Should not have
• Cheesy, in your face, aggressive

```html
<!DOCTYPE html>
<html lang="en">
<head>
<meta charset="utf-8">
<title>Membership Direct Debit Banner</title>
<link rel="stylesheet" href="https://fonts.googleapis.com/css2?family=Anton&family=Oswald:wght@500;600;700&display=swap">
<style>
  :root {
    --sky-top: #8c7a56;
    --sky-glow: #f6e7bf;
    --sky-mid: #c9b68a;
    --tree-dark: #2f3a1e;
    --grass-light: #b3c63a;
    --grass-mid: #7f9a22;
    --grass-dark: #3f5412;
    --gold-light: #fff6d2;
    --gold-mid: #d7a94a;
    --gold-deep: #7a5418;
    --ink: #141210;
    --panel-light: rgba(255, 255, 255, 0.55);
    --panel-dark: rgba(20, 18, 12, 0.82);
    --cta-yellow: #ffd21f;
  }
  html, body {
    margin: 0;
    padding: 0;
    overflow: hidden;
    background: #ffffff;
  }
  .banner {
    position: relative;
    width: 1200px;
    height: 557px;
    overflow: hidden;
  }
  .banner__photo {
    position: absolute;
    inset: 0;
    background:
      radial-gradient(ellipse 520px 300px at 880px 40px, var(--sky-glow) 0%, rgba(246,231,191,0.6) 40%, rgba(246,231,191,0) 75%),
      linear-gradient(180deg,
        var(--sky-top) 0%,
        var(--sky-mid) 38%,
        #b9a679 55%,
        var(--tree-dark) 59%,
        var(--grass-mid) 61%,
        var(--grass-light) 68%,
        var(--grass-mid) 82%,
        var(--grass-dark) 100%);
  }
  .headline-panel {
    position: absolute;
    left: 140px;
    top: 58px;
    width: 727px;
    height: 116px;
    background: var(--panel-light);
  }
  .gold-text {
    font-family: "Anton", "Oswald", sans-serif;
    text-transform: uppercase;
    background: linear-gradient(180deg, var(--gold-light) 0%, #f4dc98 35%, var(--gold-mid) 52%, var(--gold-deep) 56%, #b9852e 80%, #f0cf7a 100%);
    -webkit-background-clip: text;
    background-clip: text;
    color: transparent;
    -webkit-text-stroke: 2px var(--ink);
    filter: drop-shadow(3px 4px 3px rgba(0,0,0,0.55));
    margin: 0;
    white-space: nowrap;
  }
  .headline {
    position: absolute;
    left: 148px;
    top: 62px;
    width: 712px;
    text-align: center;
    font-size: 46px;
    line-height: 1.2;
    letter-spacing: 0.5px;
  }
  .subline {
    position: absolute;
    left: 140px;
    top: 132px;
    width: 727px;
    margin: 0;
    text-align: center;
    font-family: "Oswald", sans-serif;
    font-weight: 600;
    font-size: 23px;
    color: var(--ink);
    text-transform: uppercase;
    letter-spacing: 0.3px;
  }
  .benefits {
    position: absolute;
    left: 160px;
    top: 188px;
    width: 708px;
    text-align: center;
    font-size: 100px;
    line-height: 104px;
    -webkit-text-stroke: 2.5px var(--ink);
    letter-spacing: 2px;
  }
  .cta {
    position: absolute;
    left: 284px;
    top: 430px;
    width: 483px;
    height: 70px;
    background: var(--panel-dark);
    display: flex;
    align-items: center;
    justify-content: center;
  }
  .cta__text {
    font-family: "Oswald", sans-serif;
    font-weight: 600;
    font-size: 27px;
    color: var(--cta-yellow);
    text-transform: uppercase;
    letter-spacing: 0.3px;
  }
</style>
</head>
<body>
  <main class="banner">
    <div class="banner__photo" role="img" aria-label="Golf putter lining up a ball on a sunlit green with the flag and trees in the background"></div>

    <div class="headline-panel"></div>
    <h1 class="gold-text headline">Make the most of your membership</h1>
    <p class="subline">Spread your subscription burden across 12 months</p>

    <h2 class="gold-text benefits">Safe, Reliable<br>Convenient</h2>

    <div class="cta">
      <span class="cta__text">Talk to your club to find out how</span>
    </div>
  </main>
</body>
</html>
```